Brexalinth Web Design

We would like to have our website designed and coded. It will be a display only website - no input or output functionality. It's a fairly simple structure with not many pages, but we would like some professional design and creative elements added in to make the site attractive and sharp. I have attached a presentation with the page and content layout. Where images are included in the presentation, those are concepts that you can reorganize or layout in any way that you think looks best. Same with the wheel of services on the incubator page, and the bullet points listed on the accelerator page.

```html
<!DOCTYPE html>
<html lang="en">
<head>
<meta charset="utf-8">
<title>Brexalinth</title>
<link href="https://fonts.googleapis.com/css2?family=Heebo:wght@400;500;600;700&family=IBM+Plex+Sans:wght@500;600;700&display=swap" rel="stylesheet">
<style>
:root{
  --navy:#1a365d;
  --navy-deep:#183559;
  --steel:#3e6596;
  --ink:#111;
  --body:#222;
  --white:#fff;
  --footer:#1d1d1f;
  --hero-light:#b9b9b9;
  --hero-dark:#4a4a4a;
}
*{margin:0;padding:0;box-sizing:border-box}
html,body{width:1200px;height:2648px;overflow:hidden}
body{font-family:'Heebo',sans-serif;color:var(--body);background:var(--white);position:relative}
.abs{position:absolute}

/* hero */
.hero{left:0;top:0;width:1200px;height:643px}
.hero-photo{position:absolute;inset:0;background:linear-gradient(180deg,#8a8a8a 0%,var(--hero-light) 22%,#a4a4a4 45%,#6a6a6a 70%,var(--hero-dark) 100%)}
.brand{position:absolute;left:111px;top:17px;font-family:'IBM Plex Sans',sans-serif;font-weight:600;font-size:36px;letter-spacing:4px;color:var(--navy)}
.main-nav{position:absolute;left:459px;top:27px;font-size:15.5px;font-weight:500;color:var(--ink);display:flex;gap:11px;white-space:nowrap}
.main-nav .sep{margin:0 2px}
.hero-title{position:absolute;left:117px;top:253px;font-family:'Heebo',sans-serif;font-weight:600;font-size:52px;letter-spacing:1px;color:var(--white);line-height:1}
.hero-text{position:absolute;left:120px;top:316px;width:356px;font-size:16px;font-weight:500;line-height:27.5px;color:var(--white)}
.btn{position:absolute;background:var(--navy);color:var(--white);border-radius:24px;font-size:16px;font-weight:500;display:flex;align-items:center;justify-content:center}
.hero-btn{left:120px;top:416px;width:168px;height:46px}
.arrow{position:absolute;top:328px}
.dots{position:absolute;top:592px;left:556px;display:flex;gap:14px}
.dots span{width:12px;height:12px;border-radius:50%;background:rgba(255,255,255,.35)}
.dots span.on{background:var(--white)}

/* welcome */
.welcome{left:0;top:643px;width:1200px;height:467px;text-align:center}
.welcome h1{position:absolute;top:76px;width:100%;font-size:33px;font-weight:600;color:var(--ink)}
.welcome p{position:absolute;left:168px;top:130px;width:864px;font-size:18px;line-height:34px;color:var(--body)}
.welcome-btn{left:516px;top:336px;width:168px;height:46px}

/* services */
.services{left:0;top:1110px;width:1200px;height:557px}
.services-panel{position:absolute;left:0;top:0;width:600px;height:557px;background:var(--navy-deep);color:var(--white)}
.services-intro{position:absolute;left:115px;top:66px;width:459px;font-size:14.6px;line-height:28.2px;text-align:justify}
.services-list{position:absolute;left:115px;top:253px;list-style:none}
.services-list li{font-size:16px;font-weight:500;height:29.1px;display:flex;align-items:center;gap:4px}
.services-list svg{flex:none}
.services-close{position:absolute;left:114px;top:437px;width:460px;font-size:14.6px;line-height:26px}
.services-photo{position:absolute;left:600px;top:0;width:600px;height:557px;background:linear-gradient(180deg,#cfcfcf 0%,#bcbcbc 28%,#8f8f8f 55%,#a7a7a7 78%,#7b7b7b 100%)}

/* story */
.story{left:0;top:1667px;width:1200px;height:651px;background:var(--steel)}
.story-map{position:absolute;inset:0;background:radial-gradient(ellipse at 55% 40%,rgba(90,125,170,.35),rgba(62,101,150,0) 65%)}
.story h2{position:absolute;left:197px;top:170px;width:320px;font-family:'IBM Plex Sans',sans-serif;font-weight:600;font-size:50px;line-height:51.5px;color:var(--white)}
.story-text{position:absolute;left:531px;top:75px;width:572px;font-size:15px;font-weight:500;line-height:33.4px;color:var(--white)}

/* footer */
.footer{left:0;top:2318px;width:1200px;height:330px;background:var(--footer);color:var(--white);text-align:center}
.footer-brand{position:absolute;top:76px;width:100%;font-family:'IBM Plex Sans',sans-serif;font-weight:600;font-size:40px;letter-spacing:3px;line-height:1}
.footer-nav{position:absolute;top:151px;left:0;width:100%;display:flex;justify-content:center;gap:16px;font-size:16.5px;font-weight:500;white-space:nowrap}
.footer-nav .home{margin-right:10px}
.copy{position:absolute;top:198px;width:100%;font-size:15px}
.social-row{position:absolute;top:251px;left:501px;display:flex;gap:8px}
.social-row span{width:43px;height:43px;border-radius:50%;background:var(--white)}
</style>
</head>
<body>

<section class="abs hero">
  <div class="hero-photo" role="img" aria-label="Black and white skyline of Dubai with the tallest tower rising above the city"></div>
  <div class="brand">BREXALINTH</div>
  <nav class="main-nav">
    <span>INCUBATOR</span><span class="sep">|</span>
    <span>ACCELERATOR</span><span class="sep">|</span>
    <span>UAE DISTRIBUTION</span><span class="sep">|</span>
    <span>REFERENCES</span><span class="sep">|</span>
    <span>CONTACT US</span>
  </nav>
  <svg class="arrow" style="left:70px" width="20" height="40" viewBox="0 0 20 40"><path d="M18 2 L2 20 L18 38" fill="none" stroke="#fff" stroke-width="1.6"/></svg>
  <svg class="arrow" style="left:1108px" width="20" height="40" viewBox="0 0 20 40"><path d="M2 2 L18 20 L2 38" fill="none" stroke="#fff" stroke-width="1.6"/></svg>
  <div class="hero-title">BREXALINTH</div>
  <p class="hero-text">Lorem ipsum dolor sit amet, cotetur adipiscing elit, sed do eiusmod tempor incididunt ut labore et dolore magna aliqua.</p>
  <div class="btn hero-btn">GET STARTED</div>
  <div class="dots"><span></span><span></span><span class="on"></span><span></span></div>
</section>

<section class="abs welcome">
  <h1>WELCOME TO BREXALINTH</h1>
  <p>Brexalinth is a global incubator for start-up and early-stage medical device companies and serves as a growth accelerator for more advanced medical device companies. Located in Qamar Innovation Park, a fully integrated technology park with the aim to foster technology and entrepreneurship, Brexalinth provides active operational support to medical device companies through the expertise of highly experienced and well-connected industry veterans.</p>
  <div class="btn welcome-btn">CONTACT US</div>
</section>

<section class="abs services">
  <div class="services-panel">
    <p class="services-intro">These veterans serve as mentors, interim-managers or as freelance consultants, enabling medical device companies to outsource key operational functions, lowering monthly operating expenses and minimizing operational risks. Along with the operational support Brexalinth provides, we utilize our global network of strategic partners, distributors, manufacturers and healthcare providers to:</p>
    <ul class="services-list">
      <li><svg width="16" height="16" viewBox="0 0 16 16"><circle cx="8" cy="8" r="6.5" fill="none" stroke="#fff" stroke-width="1.6"/><circle cx="8" cy="8" r="3.5" fill="#fff"/></svg>Raise Capital</li>
      <li><svg width="16" height="16" viewBox="0 0 16 16"><circle cx="8" cy="8" r="6.5" fill="none" stroke="#fff" stroke-width="1.6"/><circle cx="8" cy="8" r="3.5" fill="#fff"/></svg>Assist and drive M&amp;A strategies</li>
      <li><svg width="16" height="16" viewBox="0 0 16 16"><circle cx="8" cy="8" r="6.5" fill="none" stroke="#fff" stroke-width="1.6"/><circle cx="8" cy="8" r="3.5" fill="#fff"/></svg>Develop global sales and marketing strategies</li>
      <li><svg width="16" height="16" viewBox="0 0 16 16"><circle cx="8" cy="8" r="6.5" fill="none" stroke="#fff" stroke-width="1.6"/><circle cx="8" cy="8" r="3.5" fill="#fff"/></svg>Build and expand distribution channels</li>
      <li><svg width="16" height="16" viewBox="0 0 16 16"><circle cx="8" cy="8" r="6.5" fill="none" stroke="#fff" stroke-width="1.6"/><circle cx="8" cy="8" r="3.5" fill="#fff"/></svg>Source suppliers and assist in outsourcing production</li>
      <li><svg width="16" height="16" viewBox="0 0 16 16"><circle cx="8" cy="8" r="6.5" fill="none" stroke="#fff" stroke-width="1.6"/><circle cx="8" cy="8" r="3.5" fill="#fff"/></svg>Support in Regulatory Affairs</li>
    </ul>
    <p class="services-close">Brexalinth helps your business minimize operational risk, operate more cost-effective, grow faster and increase profitability.</p>
  </div>
  <div class="services-photo" role="img" aria-label="Historic black and white photo of a Dubai shoreline with fishing boats and people on the beach"></div>
</section>

<section class="abs story">
  <div class="story-map" role="img" aria-label="Faint world map with connection lines radiating from Dubai"></div>
  <h2>Located in Dubai – Covering the world</h2>
  <div class="story-text">
    <p>The story of Dubai - from a small fishing village of palm frond huts to the most modern city in the world.</p>
    <p>In a matter of 20 years Dubai has shown the world what ambition, vision and leadership, coupled with determination to overcome the odds, can achieve.</p>
    <p>The story of Dubai symbolizes the ambition of many corporations and leaders around the globe.</p>
    <p>We are proud to call Dubai our home for the past 20 years, having witnessed the most dynamic phase of that growth.</p>
    <p>The Dubai story has inspired the founding of Brexalinth.&nbsp; A globally connected company, driven by passionate medical device industry experts, aiming for the exceptional and never the average.</p>
    <p>Connecting the global medical device world, helping young and established medical device companies to accelerate.&nbsp; Always with the goal to become the best - as impossible as it might seem.</p>
    <p>Dubai has shown the world – It is not impossible!</p>
  </div>
</section>

<footer class="abs footer">
  <div class="footer-brand">BREXALINTH</div>
  <nav class="footer-nav">
    <span class="home">HOME</span>
    <span>INCUBATOR</span><span>|</span>
    <span>ACCELERATOR</span><span>|</span>
    <span>UAE DISTRIBUTION</span><span>|</span>
    <span>REFERENCES</span><span>|</span>
    <span>CONTACT US</span>
  </nav>
  <div class="copy">©Copyright Brexalinth . All Rights Reserved.</div>
  <div class="social-row"><span></span><span></span><span></span><span></span></div>
</footer>

</body>
</html>
```